Vantor Reach Unique Marketing Website Design

I am starting a new company that is a thought leader in the marketing consulting space. The company is called Vantor Reach. We intend to build a Wordpress site on the Astra Theme with the Spectra builder. Our goal is to become the leading voice that empowers high-ticket service business leaders to become Vantor Reach by equipping them with the cutting-edge frameworks and decision grade intelligence taught in leading business schools. What we are looking for is a website design that is clean and professional, making some use of white space well also being eye catching and distinctive in the consulting space. We will probably want to have a video on the homepage not in the hero section, but just below to explain the company and what we do. Our tagline is "Be found. Be chosen." I have attached a brand guide with some messaging, our typography choices, and our color system. The full site will have a primary nav that is four pages - About us, Services, Insights (essentially a blog), and Contact Us. The goal of this project is to develop an art direction that I can give to a designer to build loads of new pages.

Target Market(s)

Business owners (mostly male) from 30-60 years old, looking to fix their sales and marketing funnel.

Industry/Entity Type

Marketing consulting

Font styles to use
Sans Serif

Requirements
Must have
• A clean, professional design that builds trust with owners of high-ticket service businesses. We need a space for explainer video, and sections that tell prospects what we do. Would also like to have a blog carousel.
Nice to have
• Social feeds, if possible. See attached documents for colors and fonts.
Should not have
• Our feel is professional enough to be trustworthy, but unique enough to be memorable. Cartoon ideas do not meet the professional test, and we do not want the website to appear feminine.

```html
<!DOCTYPE html>
<html lang="en">
<head>
<meta charset="utf-8">
<title>Vantor Reach — Be Found. Be Chosen.</title>
<link href="https://fonts.googleapis.com/css2?family=Bebas+Neue&family=Inter:wght@400;500;600;700;800;900&family=Archivo+Black&family=Libre+Baskerville:ital,wght@0,400;0,700;1,400&family=Gochi+Hand&family=Oswald:wght@500;600&display=swap" rel="stylesheet">
<style>
:root{
  --navy:#0e1630;
  --navy-deep:#0a1128;
  --blue:#2f5bf5;
  --purple:#8b5cf6;
  --ink:#111827;
  --muted:#5b6475;
  --white:#ffffff;
  --line:#e5e7eb;
}
*{box-sizing:border-box;margin:0;padding:0}
html,body{width:1200px;height:4326px;overflow:hidden}
body{font-family:'Inter',sans-serif;color:var(--ink);background:var(--white);position:relative}
.hand{font-family:'Gochi Hand',cursive}

/* nav */
.site-nav{position:absolute;top:0;left:0;width:1200px;height:56px;background:#fff}
.brand{display:flex;align-items:center;gap:10px;font-weight:600;font-size:22px;color:var(--navy)}
.brand-mark{width:28px;height:28px;background:var(--navy)}
.site-nav .brand{position:absolute;left:114px;top:12px}
.nav-links{position:absolute;left:676px;top:20px;font-size:11px;font-weight:600}
.nav-links a{color:var(--ink);text-decoration:none;position:absolute;white-space:nowrap}
.nav-btn{position:absolute;left:993px;top:13px;width:94px;height:29px;background:var(--blue);color:#fff;font-size:11px;font-weight:700;display:flex;align-items:center;justify-content:center;border-radius:2px}

/* hero */
.hero{position:absolute;top:56px;left:0;width:1200px;height:691px;overflow:hidden;
  background:linear-gradient(90deg,#8e96a6 0%,#b9c0cc 30%,#c8cfd9 55%,#a9b1bf 80%,#8b93a2 100%)}
.hero-photo{position:absolute;inset:0;background:radial-gradient(ellipse at 60% 30%,rgba(120,170,230,.35),transparent 55%)}
.hero-fade{position:absolute;inset:0;background:linear-gradient(180deg,rgba(255,255,255,.15) 0%,rgba(255,255,255,.55) 60%,rgba(255,255,255,.85) 100%)}
.hero-note{position:absolute;top:44px;left:0;width:1200px;text-align:center;font-size:17px;color:#6d5df0;transform:rotate(-4deg)}
.hero-title{position:absolute;left:0;width:1200px;text-align:center;font-family:'Bebas Neue',sans-serif;font-size:140px;line-height:1;letter-spacing:-1px}
.t1{top:115px;color:var(--navy-deep)}
.t2{top:230px;color:var(--blue)}
.hero-copy{position:absolute;top:384px;left:320px;width:560px;text-align:center;font-size:18px;line-height:30px;color:#2b3342}
.btn{position:absolute;display:flex;align-items:center;justify-content:center;font-size:13px;font-weight:700;height:56px}
.btn-dark{left:411px;top:536px;width:176px;background:var(--navy-deep);color:#fff}
.btn-ghost{left:607px;top:536px;width:177px;border:2px solid var(--navy-deep);color:var(--navy-deep)}

/* ticker */
.ticker{position:absolute;top:747px;left:0;width:1200px;height:48px;background:var(--purple);display:flex;align-items:center;white-space:nowrap;overflow:hidden;font-family:'Oswald',sans-serif;font-weight:500;color:#fff;font-size:19px;letter-spacing:2px}
.ticker span{margin-left:-8px}

/* video */
.video-sec{position:absolute;top:795px;left:0;width:1200px;height:811px;background:var(--navy-deep)}
.sec-title{position:absolute;left:0;width:1200px;text-align:center;font-weight:700;font-size:36px}
.sec-sub{position:absolute;left:0;width:1200px;text-align:center;font-size:17px}
.video-frame{position:absolute;left:159px;top:217px;width:878px;height:493px;border:3px solid #1f2740;border-radius:6px;box-shadow:0 0 60px rgba(90,80,240,.45);overflow:hidden}
.video-still{position:absolute;inset:0;background:linear-gradient(135deg,#1b2440 0%,#3a4560 40%,#7a6f63 75%,#b2a595 100%)}
.play{position:absolute;left:50%;top:50%;width:76px;height:76px;margin:-38px 0 0 -38px;border-radius:50%;background:rgba(255,255,255,.18)}
.live{position:absolute;left:24px;bottom:24px;color:#fff;font-size:11px;font-weight:700;letter-spacing:1px;display:flex;align-items:center;gap:10px}
.live i{width:10px;height:10px;border-radius:50%;background:#ef4444;display:block}
.badge{position:absolute;left:910px;top:1328px;width:158px;height:126px;background:#fff;border-radius:8px;transform:rotate(3deg);padding:26px 20px;box-shadow:0 10px 30px rgba(0,0,0,.4);font-size:11px;font-weight:800;line-height:13px;color:var(--ink)}

/* pillars */
.pillars{position:absolute;top:1606px;left:0;width:1200px;height:931px;background:#fff}
.pillar{position:absolute;top:215px;width:470px;height:481px;border-radius:14px;color:#fff;padding:48px 48px;overflow:hidden}
.pillar.blue{left:109px;background:var(--blue)}
.pillar.purple{left:617px;background:var(--purple)}
.pillar-icon{width:62px;height:62px;border-radius:8px;background:rgba(255,255,255,.25);display:flex;align-items:center;justify-content:center}
.pillar-ghost{position:absolute;right:42px;top:42px;width:110px;height:110px;border-radius:12px;background:rgba(255,255,255,.14)}
.pillar h3{font-family:'Archivo Black',sans-serif;font-size:27px;line-height:30px;margin-top:30px;font-weight:400}
.pillar p{font-size:15px;line-height:25px;margin-top:14px}
.pillar ul{list-style:none;margin-top:42px;font-size:10.5px;font-weight:800;letter-spacing:1px}
.pillar li{margin-bottom:15px}
.pillar li::before{content:"•";margin-right:10px}
.quote{position:absolute;top:2380px;left:0;width:1200px;text-align:center;font-family:'Libre Baskerville',serif;font-style:italic;font-size:22px;line-height:37px;color:var(--ink)}

/* stats */
.stats{position:absolute;top:2537px;left:0;width:1200px;height:223px;background:var(--navy-deep);color:#fff}
.stat{position:absolute;top:68px}
.stat-label{font-size:9.5px;font-weight:800;letter-spacing:3px;color:var(--purple);line-height:13px}
.stat-value{font-family:'Bebas Neue',sans-serif;font-size:52px;line-height:48px;margin-top:6px}
.stat-value.sm{font-family:'Oswald',sans-serif;font-weight:600;font-size:28px;line-height:32px}
.stat-note{font-size:11px;color:#8e97ad;margin-top:6px;line-height:15px}
.divider{position:absolute;top:60px;width:1px;height:110px;background:#2a3352}

/* insights */
.insights-h{position:absolute;top:2856px;left:109px;font-family:'Archivo Black',sans-serif;font-size:28px;color:var(--ink);font-weight:400}
.insights-s{position:absolute;top:2900px;left:109px;font-size:16px;color:var(--purple)}
.post{position:absolute;top:2962px;width:305px;height:428px;border:1px solid var(--line);border-radius:6px;background:#fff;box-shadow:0 4px 14px rgba(0,0,0,.05)}
.post-img{position:absolute;left:6px;top:10px;width:293px;height:183px;border-radius:6px}
.post-tag{position:absolute;left:25px;top:222px;font-size:8px;font-weight:800;letter-spacing:1px;color:var(--purple)}
.post h4{position:absolute;left:25px;top:244px;width:260px;font-family:'Libre Baskerville',serif;font-size:16px;line-height:24px;font-weight:400;color:var(--ink)}
.post p{position:absolute;left:25px;top:312px;width:260px;font-size:12px;line-height:18px;color:var(--muted)}
.post .more{position:absolute;left:25px;font-size:11px;font-weight:800;letter-spacing:1px;color:var(--ink)}

/* cta */
.cta{position:absolute;top:3490px;left:0;width:1200px;height:509px;background:var(--purple);color:#fff;text-align:center}
.cta h2{position:absolute;top:116px;left:0;width:1200px;font-family:'Bebas Neue',sans-serif;font-size:70px;line-height:56px;font-weight:400}
.cta .lead{position:absolute;top:240px;left:0;width:1200px;font-size:18px;line-height:25px}
.cta-btn{position:absolute;top:319px;left:461px;width:272px;height:56px;background:#fff;color:var(--navy-deep);border-radius:8px;font-size:14px;font-weight:800;display:flex;align-items:center;justify-content:center;letter-spacing:-.3px}
.cta .fine{position:absolute;top:393px;left:0;width:1200px;font-size:12px;color:#d9ccff}

/* footer */
.site-footer{position:absolute;top:3999px;left:0;width:1200px;height:327px;background:var(--navy-deep);color:#fff}
.site-footer .brand{position:absolute;left:112px;top:52px;color:#fff;font-size:18px}
.site-footer .brand-mark{background:#fff;width:24px;height:24px}
.foot-about{position:absolute;left:109px;top:92px;width:250px;font-size:11px;line-height:18px;color:#9aa3b8}
.foot-col{position:absolute;top:50px}
.foot-col h5{font-size:9.5px;font-weight:800;letter-spacing:2px;margin-bottom:20px}
.foot-col a{display:block;font-size:11px;color:#9aa3b8;text-decoration:none;margin-bottom:16px}
.copy{position:absolute;top:262px;left:0;width:1200px;text-align:center;font-size:9.5px;color:#9aa3b8}
</style>
</head>
<body>

<header class="site-nav">
  <div class="brand"><span class="brand-mark"></span>Vantor Reach</div>
  <nav class="nav-links">
    <a style="left:0">Services</a>
    <a style="left:76px">About Us</a>
    <a style="left:153px">Insights</a>
    <a style="left:227px">Contact Us</a>
  </nav>
  <div class="nav-btn">Book a Call</div>
</header>

<section class="hero">
  <div class="hero-photo" role="img" aria-label="Executives in a boardroom with a floating analytics display"></div>
  <div class="hero-fade"></div>
  <div class="hero-note hand">Your deals aren't dying because of price. They're dying in the Blind Spot</div>
  <h1 class="hero-title t1">BE FOUND.</h1>
  <div class="hero-title t2">BE CHOSEN.</div>
  <p class="hero-copy">We teach high-ticket service businesses the Fortune 500-level frameworks for why qualified buyers don't choose you, and how to design buying experiences where full commitment is the only logical conclusion.</p>
  <div class="btn btn-dark">Get the Diagnosis</div>
  <div class="btn btn-ghost">See How It Works</div>
</section>

<div class="ticker"><span>MING &nbsp;•&nbsp;&nbsp;&nbsp; PIPELINE BLIND SPOT &nbsp;•&nbsp;&nbsp;&nbsp; VERDICT-READY INSIGHT &nbsp;•&nbsp;&nbsp;&nbsp; CHOICE DESIGN &nbsp;•&nbsp;&nbsp;&nbsp; TRUST FRAMING &nbsp;•&nbsp;&nbsp;&nbsp; PIPELINE BLIND SPOT</span></div>

<section class="video-sec">
  <h2 class="sec-title" style="top:93px;color:#fff">Here's what they won't tell you in the textbook</h2>
  <div class="sec-sub hand" style="top:145px;color:#7c6cf5">Most of what you learned about marketing is lighting money on fire.</div>
  <div class="video-frame">
    <div class="video-still" role="img" aria-label="Hands on a laptop showing a marketing analytics dashboard"></div>
    <div class="play"><svg width="76" height="76" viewBox="0 0 76 76"><path d="M32 26 L50 38 L32 50 Z" fill="#fff"/></svg></div>
    <div class="live"><i></i>THE BLIND SPOT EXPLAINED—LIVE</div>
  </div>
</section>
<div class="badge">
  <svg width="26" height="20" viewBox="0 0 26 20"><path d="M13 2 L25 8 L13 14 L1 8 Z" fill="#111827"/><path d="M6 11 V16 Q13 20 20 16 V11 L13 15 Z" fill="#111827"/></svg>
  <div style="margin-top:6px">BUSINESS SCHOOL FRAMEWORKS,<br>ZERO JARGON</div>
</div>

<section class="pillars">
  <h2 class="sec-title" style="top:96px;color:var(--ink)">The two things every scaling business needs</h2>
  <div class="sec-sub hand" style="top:146px;color:#4b5563;font-size:15px">And why most consultants only give you half the picture.</div>

  <article class="pillar blue">
    <div class="pillar-ghost"></div>
    <div class="pillar-icon"><svg width="24" height="20" viewBox="0 0 24 20"><path d="M1 3 H9 L11 5 H23 V19 H1 Z" fill="#fff"/><path d="M12 8 L13 11 L16 11 L13.6 13 L14.5 16 L12 14 L9.5 16 L10.4 13 L8 11 L11 11 Z" fill="#2f5bf5"/></svg></div>
    <h3>BUYER SIGNAL<br>MAPPING</h3>
    <p>We build dossiers on what's actually happening in your buyer's journey. Not what you hope—what's really happening when deals stall, or go dark.</p>
    <ul>
      <li>WHY YOUR QUALIFIED LEADS GHOST YOU</li>
      <li>WHERE TRUST FRICTION KILLS MOTIVATION</li>
      <li>THE REAL REASON DEALS TAKE 3X LONGER</li>
    </ul>
  </article>

  <article class="pillar purple">
    <div class="pillar-ghost" style="border-radius:55px 55px 14px 14px"></div>
    <div class="pillar-icon"><svg width="22" height="22" viewBox="0 0 22 22"><circle cx="11" cy="11" r="10" fill="#fff"/><rect x="10" y="9" width="2" height="8" fill="#8b5cf6"/><circle cx="11" cy="6" r="1.3" fill="#8b5cf6"/></svg></div>
    <h3>CHOICE<br>DESIGN</h3>
    <p>We apply behavioral science to engineer buying experiences where saying yes feels safer than saying no. This is the stuff Nobel Prize winners discovered—made practical for your business.</p>
    <ul>
      <li>HOW BUYERS ACTUALLY MAKE HIGH-STAKES DECISIONS</li>
      <li>BUILDING TRUST THAT COMPOUNDS OVER TIME</li>
      <li>MAKING "YES" THE ONLY LOGICAL CONCLUSION</li>
    </ul>
  </article>
</section>
<p class="quote">"Intelligence tells you what's true. Psychology tells you what to do<br>about it. You need both—or you're flying blind."</p>

<section class="stats">
  <div class="stat" style="left:109px;top:62px">
    <div class="stat-label">REVENUE GENERATED USING THESE<br>METHODS</div>
    <div class="stat-value">$200M+</div>
    <div class="stat-note">Across 14+ industries, 3 continents</div>
  </div>
  <div class="divider" style="left:432px"></div>
  <div class="stat" style="left:468px">
    <div class="stat-label">FOUNDER BACKGROUND</div>
    <div class="stat-value sm">Exited Entrepreneur</div>
    <div class="stat-note">+ University professor who trains top-<br>tier consultants</div>
  </div>
  <div class="divider" style="left:740px"></div>
  <div class="stat" style="left:775px;top:62px">
    <div class="stat-label">WHAT YOU GET</div>
    <div class="stat-value sm">VERDICT-READY<br>INSIGHT</div>
    <div class="stat-note">Not dashboards. Answers.</div>
  </div>
</section>

<h2 class="insights-h">LATEST INSIGHTS</h2>
<div class="insights-s hand">The stuff you won't find in a typical marketing blog</div>

<article class="post" style="left:109px">
  <div class="post-img" role="img" aria-label="Business professionals working at laptops" style="background:linear-gradient(135deg,#5d6b7d,#c9cfd6 60%,#8b949f)"></div>
  <div class="post-tag">HOT TAKE</div>
  <h4>The 3 Binary Decisions Every High-Ticket Buyer Makes</h4>
  <p>Spoiler: It's not "Do I want this?" It's "Can I trust this person to solve my problem without creating new ones?"</p>
  <div class="more" style="top:385px">READ THIS →</div>
</article>
<article class="post" style="left:445px">
  <div class="post-img" role="img" aria-label="Team brainstorming at a wall of sticky notes" style="background:linear-gradient(135deg,#e8e6e1,#cfc9c0 50%,#b09c8a)"></div>
  <div class="post-tag">BUYER BEHAVIOR</div>
  <h4>Why Comparison Shopping Is the Death of Authority</h4>
  <p>The moment someone compares you, you've already lost. Here's what to do instead.</p>
  <div class="more" style="top:365px">READ THIS →</div>
</article>
<article class="post" style="left:780px">
  <div class="post-img" role="img" aria-label="Laptop displaying an analytics dashboard" style="background:linear-gradient(135deg,#3a4352,#9aa6b4 50%,#d3d8de)"></div>
  <div class="post-tag">CASE STUDY</div>
  <h4>How We Reclaimed $2.4M Hiding in "Lost" Deals</h4>
  <p>A boutique consultancy thought their leads were bad. Turns out, their buying experience was just terrifying.</p>
  <div class="more" style="top:385px">READ THIS →</div>
</article>

<section class="cta">
  <h2>STOP GUESSING. START<br>KNOWING.</h2>
  <p class="lead">Most businesses have no idea why qualified buyers don't choose them.<br>You're about to be the exception.</p>
  <div class="cta-btn">GET YOUR FREE DIAGNOSIS</div>
  <div class="fine hand">No pitch. No pressure. Just clarity.</div>
</section>

<footer class="site-footer">
  <div class="brand"><span class="brand-mark"></span>Vantor Reach</div>
  <p class="foot-about">Teaching high-ticket service businesses the Fortune 500-level frameworks for why qualified buyers don't choose you—and what to do about it.</p>
  <div class="foot-col" style="left:861px">
    <h5>NAVIGATE</h5>
    <a>Services</a><a>About Us</a><a>Insights</a><a>Contact Us</a>
  </div>
  <div class="foot-col" style="left:1004px">
    <h5>LEGAL</h5>
    <a>Privacy Policy</a><a>Terms of Service</a>
  </div>
  <div class="copy">© 2026 Vantor Reach. Be Found. Be Chosen.</div>
</footer>

</body>
</html>
```